Global Educational start-up needs elegant website

Hi,
I am looking for a website for a company which is serving the high-end, demanding clients in China, on educational market and working internationally. The company name is Amber Harbor Educational Services. Please find attached its logo.
We need a website consisting of seven sites:
1. What do we do? (main/basic site)
2. Programs (two subsites under this site)
a) Leadership, Entrepreneurship and Personal Development (Europe)
b) Career incubator (UK)
3. Our mission and values
4. Who are we?
5. Testimonials
6. Contact us
7. Sign for a program! (button redirecting to a form)
We would appreciate simplicity, elegance and minimalizm. It should be interactive and should meet highest expectations of the rich cusomers. On the visual materials the Chinese children aged 13-20 are preferred, in link with education, development and so on.
Time is short so we might finish the contest in a moment we find a proper choice.
Target Market(s)
Parents of rich Chinese children.
Industry/Entity Type
Education

```html
<!DOCTYPE html>
<html lang="en">
<head>
<meta charset="utf-8">
<title>Amber Harbor Educational Services</title>
<link href="https://fonts.googleapis.com/css2?family=Open+Sans:wght@400;600;700&family=Oswald:wght@400&display=swap" rel="stylesheet">
<style>
:root{
  --green:#3f9a2f;
  --green-dark:#2f7d22;
  --footer-green:#4f9a45;
  --slate:#56555b;
  --slate-dark:#4a4950;
  --beige:#e3dcc1;
  --ink:#333;
  --muted:#666;
  --white:#fff;
}
*{box-sizing:border-box;margin:0;padding:0}
html,body{width:918px;height:1200px;overflow:hidden;background:var(--white)}
body{font-family:"Open Sans",Arial,sans-serif;color:var(--ink);position:relative}
.abs{position:absolute}
.site-header{position:absolute;left:0;top:0;width:918px;height:70px;background:linear-gradient(#fff,#e4e4e4)}
.header-green{left:0;top:0;width:110px;height:70px;background:var(--green)}
.brand{left:100px;top:0;width:260px;height:70px;background:#fff;border-radius:35px 0 0 35px;display:flex;align-items:center;padding-left:14px;gap:10px}
.brand-mark{width:40px;height:40px;border-radius:50%;border:3px solid #555;flex:none}
.brand-name{color:#555;font-weight:400;font-size:17px;line-height:1.05;letter-spacing:.3px}
.brand-name small{display:block;font-size:7.5px;letter-spacing:2.6px;margin-top:2px}
.main-nav{left:365px;top:24px;display:flex;align-items:center;gap:20px;font-size:10.5px;color:#444}
.nav-home{width:22px;height:22px;background:var(--green);display:flex;align-items:center;justify-content:center}
.top-bar{left:0;top:70px;width:918px;height:52px}
.call-text{left:164px;top:85px;color:#fff;font-size:14.5px;letter-spacing:.3px}
.call-text b{font-weight:700}
.call-icon{left:120px;top:79px;width:32px;height:32px;border:1px solid rgba(255,255,255,.7);border-radius:50%;display:flex;align-items:center;justify-content:center}
.sign-btn{left:686px;top:78px;width:132px;height:23px;border:1px solid #ddd;border-radius:2px;color:#fff;font-size:12px;display:flex;align-items:center;justify-content:center}
.hero{left:0;top:109px;width:918px;height:413px;background:linear-gradient(90deg,#6f6a63 0%,#9b958c 30%,#bdb6a8 45%,#3f5a9a 55%,#2f4f96 68%,#c4bdb2 80%,#7c756c 100%)}
.hero-caption{left:0;top:474px;width:918px;height:48px}
.hero-caption p{position:absolute;left:325px;top:11px;font-family:"Oswald",sans-serif;font-size:17.5px;color:#fff;letter-spacing:-.2px}
.dots{left:162px;top:489px;display:flex;gap:5px}
.dots i{width:11px;height:11px;border-radius:50%;background:rgba(255,255,255,.55)}
.dots i.on{background:var(--green)}
.hero-rule{left:0;top:523px;width:918px;height:2px;background:#ddd}
.feature{top:548px;width:230px;text-align:center}
.feature-badge{width:90px;height:90px;margin:0 auto;border-radius:50%;background:radial-gradient(circle at 50% 40%,#4cae36,var(--green-dark));border:3px solid #fff;box-shadow:0 2px 6px rgba(0,0,0,.35);display:flex;align-items:center;justify-content:center}
.feature h2{font-weight:400;font-size:14.5px;color:#222;margin-top:12px;letter-spacing:.2px}
.feature p{font-size:10.3px;color:var(--muted);line-height:16px;margin:7px auto 0;width:196px}
.btn-dark{display:inline-block;margin-top:9px;background:#3c3b40;color:#fff;font-size:10.5px;padding:3px 7px;border-radius:2px;box-shadow:0 1px 2px rgba(0,0,0,.4)}
.col-rule{top:560px;width:1px;height:150px;background:linear-gradient(transparent,#ddd,transparent)}
.about{left:0;top:762px;width:918px;height:258px}
.welcome{left:101px;top:778px;color:#fff;width:400px}
.welcome h2{font-weight:400;font-size:17px}
.welcome h2 span{font-size:21px}
.welcome p{font-size:9.9px;line-height:15.2px;margin-top:6px;color:#f2f2f2}
.welcome p.narrow{width:365px;margin-top:10px}
.btn-green{left:101px;top:989px;width:77px;height:31px;background:var(--green);color:#fff;font-size:10.5px;display:flex;align-items:center;justify-content:center}
.contact-form{left:608px;top:778px;width:210px}
.contact-form h2{text-align:right;font-weight:400;font-size:21px;color:#333}
.field{position:absolute;left:0;width:210px;height:22px;background:#fff;border:1px solid #d8d2b8;font-size:9.5px;color:#666;padding:4px 7px}
.submit{left:740px;top:989px;width:78px;height:31px;background:#111;color:#fff;font-size:13px;display:flex;align-items:center;justify-content:center}
.site-footer{left:0;top:1022px;width:918px;height:178px;background:var(--footer-green);color:#fff}
.f-col h3{font-weight:600;font-size:13px}
.f-col .rule{height:1px;background:rgba(255,255,255,.35);margin-top:4px}
.f-links{list-style:none;margin-top:6px;font-size:10px;white-space:nowrap}
.f-links li{height:20px;display:flex;align-items:center;gap:7px}
.f-links li::before{content:"";border-left:4px solid #fff;border-top:3px solid transparent;border-bottom:3px solid transparent}
.f-rule{top:1020px;width:1px;height:138px;background:rgba(0,0,0,.12)}
.contact-item{position:absolute;font-size:10px;line-height:16px;display:flex;gap:10px}
.social{position:absolute;left:492px;display:flex;align-items:center;gap:17px;font-size:10px}
.social i{width:22px;height:22px;background:#2d5f8f;display:block}
.copy{left:618px;top:1127px;width:200px;text-align:center;font-size:10px;line-height:15px}
.copy-mark{left:674px;top:1030px;width:88px;height:88px;border-radius:50%;border:4px solid #367a2e}
</style>
</head>
<body>

<header class="site-header">
  <div class="abs header-green"></div>
  <div class="abs brand">
    <span class="brand-mark"></span>
    <span class="brand-name">AMBER HARBOR<small>EDUCATIONAL SERVICES</small></span>
  </div>
  <nav class="abs main-nav">
    <span class="nav-home"><svg width="12" height="12" viewBox="0 0 12 12"><path d="M6 1L1 6h1.5v5h3V8h1v3h3V6H11z" fill="#fff"/></svg></span>
    <span>What we do</span><span>Programs</span><span>Our mission and values</span><span>Who are we?</span><span>Contact Us</span>
  </nav>
</header>

<svg class="abs top-bar" width="918" height="52" viewBox="0 0 918 52">
  <rect x="0" y="0" width="918" height="39" fill="var(--slate-dark)"/>
  <polygon points="0,0 404,0 376,52 0,52" fill="var(--green)"/>
</svg>
<div class="abs call-icon"><svg width="14" height="14" viewBox="0 0 14 14"><path d="M3 1l2 3-1.3 1.3c.8 1.8 2.2 3.2 4 4L9 8l3 2-1.5 2.5C6 12 2 8 1.5 2.5z" fill="#fff"/></svg></div>
<div class="abs call-text">CALL US NOW : <b>0198765432</b></div>
<svg class="abs" style="left:660px;top:81px" width="16" height="16" viewBox="0 0 16 16"><path d="M2 1h8l3 3v4M2 1v14h6" fill="none" stroke="#fff" stroke-width="1.5"/><path d="M9 13l5-5 1.5 1.5-5 5H9z" fill="#fff"/></svg>
<div class="abs sign-btn">Sign for a program!</div>

<div class="abs hero" role="img" aria-label="Smiling student in a blue cardigan holding yellow folders, leaning on a pillar in a campus corridor"></div>
<svg class="abs hero-caption" width="918" height="48" viewBox="0 0 918 48"><polygon points="316,0 918,0 918,48 280,48" fill="rgba(70,68,76,.85)"/></svg>
<div class="abs hero-caption"><p>We are serving the high-end, demanding clients in China on educational market</p></div>
<div class="abs dots"><i class="on"></i><i></i><i></i><i></i><i></i></div>
<div class="abs hero-rule"></div>

<section>
  <div class="abs feature" style="left:78px">
    <div class="feature-badge"><svg width="42" height="42" viewBox="0 0 42 42" fill="#fff"><circle cx="14" cy="14" r="7"/><circle cx="26" cy="27" r="10"/><circle cx="26" cy="27" r="4" fill="#3f9a2f"/><circle cx="14" cy="14" r="2.5" fill="#3f9a2f"/></svg></div>
    <h2>PROGRAMS</h2>
    <p>Lorem ipsum dolodsr sitd amet, cdonse ctetuer adipiscingads ealit mag na aliq</p>
    <span class="btn-dark">Read More</span>
  </div>
  <div class="abs col-rule" style="left:324px"></div>
  <div class="abs feature" style="left:344px">
    <div class="feature-badge"><svg width="44" height="44" viewBox="0 0 44 44" fill="none" stroke="#fff" stroke-width="3"><circle cx="22" cy="22" r="18"/><circle cx="22" cy="22" r="10"/><circle cx="22" cy="22" r="3" fill="#fff"/></svg></div>
    <h2>OUR MISSION AND VALUES</h2>
    <p>Lorem ipsum dolodsr sitd amet, cdonse ctetuer adipiscingads ealit mag na aliq</p>
    <span class="btn-dark">Read More</span>
  </div>
  <div class="abs col-rule" style="left:590px"></div>
  <div class="abs feature" style="left:611px">
    <div class="feature-badge"><svg width="46" height="40" viewBox="0 0 46 40" fill="#fff"><circle cx="12" cy="7" r="4"/><circle cx="23" cy="6" r="4.5"/><circle cx="34" cy="7" r="4"/><rect x="8" y="12" width="8" height="16" rx="2"/><rect x="19" y="12" width="8" height="17" rx="2"/><rect x="30" y="12" width="8" height="16" rx="2"/><path d="M3 28q20 14 40 0v4q-20 12-40 0z"/></svg></div>
    <h2>WHO ARE WE?</h2>
    <p>Lorem ipsum dolodsr sitd amet, cdonse ctetuer adipiscingads ealit mag na aliq</p>
    <span class="btn-dark">Read More</span>
  </div>
</section>

<svg class="abs about" width="918" height="258" viewBox="0 0 918 258">
  <rect width="918" height="258" fill="var(--beige)"/>
  <polygon points="0,0 574,0 468,258 0,258" fill="var(--slate)"/>
  <line x1="577" y1="0" x2="471" y2="258" stroke="#fff" stroke-width="3"/>
</svg>
<div class="abs welcome">
  <h2>Welcome to <span>AMBER HARBOR</span></h2>
  <p>Lorem ipsum dolor sit amet, consectetuer adipiscing elit, sed diam nonummy nibh int euismod tincidunt ut laoreet dolore magna aliquam erat volutpat. Ut wisi enim adsps minim veniam, quis nostrud exerci tation ullamcorper suscipit lobortis nisl ut aliquips ex ea commodo consequat. Duis autem vel eum iriure dolor in hendrerit in vulputatei velit esse molestie consequat, vel illum dolore eu feugiat nulla facilisis at vero eros et accumsan et iusto odio dignissim qui blandit praesent luptatum zzril delenit augue ad duis dolore te feugait nulla facilisi.Ut wisi enim ad minim veniam, quis nostrud.</p>
  <p class="narrow">Lorem ipsum dolor sit amet, consectetuer adipiscing elit, sed diam nonummy nibh int euismod tincidunt ut laoreet dolore magna aliquam erat volutpat. Ut wisi enim ut aliquips ex ea commodo consequat.</p>
</div>
<div class="abs btn-green">Read More</div>

<form class="abs contact-form">
  <h2>GET IN TOUCH</h2>
  <div class="field" style="top:40px">Your Name*</div>
  <div class="field" style="top:70px">Your Phone Number*</div>
  <div class="field" style="top:102px">Your Email *</div>
  <div class="field" style="top:134px;height:56px">Your Message</div>
</form>
<div class="abs submit">Submit</div>

<footer class="abs site-footer"></footer>
<div class="abs f-col" style="left:101px;top:1039px;width:115px;color:#fff">
  <h3>Quick Links</h3><div class="rule"></div>
  <ul class="f-links"><li>Home</li><li>What we do</li><li>Programs</li><li>Our mission and values</li><li>Who are we?</li><li>Contact Us</li></ul>
</div>
<div class="abs f-rule" style="left:242px;top:1042px"></div>
<div class="abs f-col" style="left:273px;top:1039px;width:156px;color:#fff">
  <h3>Contact Us</h3><div class="rule"></div>
</div>
<div class="contact-item" style="left:270px;top:1066px;color:#fff"><svg width="12" height="16" viewBox="0 0 12 16"><path d="M6 0a6 6 0 016 6c0 4-6 10-6 10S0 10 0 6a6 6 0 016-6z" fill="#fff"/><circle cx="6" cy="6" r="2.2" fill="#4f9a45"/></svg><span style="margin-left:3px">Lorem ipsum do consectetuer<br>adipiscing elitUt wisi enim ad<br>ST 56 - 54</span></div>
<div class="contact-item" style="left:271px;top:1123px;color:#fff"><svg width="11" height="12" viewBox="0 0 14 14"><path d="M3 1l2 3-1.3 1.3c.8 1.8 2.2 3.2 4 4L9 8l3 2-1.5 2.5C6 12 2 8 1.5 2.5z" fill="#fff"/></svg><span>0198765432</span></div>
<div class="contact-item" style="left:270px;top:1150px;color:#fff"><svg width="14" height="12" viewBox="0 0 14 12"><path d="M1 5l6-4 6 4v7H1z" fill="#fff"/><path d="M1 5l6 4 6-4" fill="none" stroke="#4f9a45"/></svg><span>info@amberharbor-edu.example</span></div>
<div class="abs f-rule" style="left:458px;top:1042px"></div>
<div class="abs f-col" style="left:492px;top:1039px;color:#fff"><h3>Follow Us On</h3></div>
<div class="social" style="top:1069px;color:#fff"><i></i>Chatterly</div>
<div class="social" style="top:1098px;color:#fff"><i style="background:#3aa7e0"></i>Chirpline</div>
<div class="social" style="top:1128px;color:#fff"><i style="background:#e8e8e8"></i>Streamora</div>
<div class="social" style="top:1158px;color:#fff"><i style="background:#1f7bb5"></i>Workwide</div>
<div class="abs f-rule" style="left:610px;top:1042px"></div>
<div class="abs copy-mark"></div>
<div class="abs copy" style="color:#fff">© 2014. <b>Amber Harbor</b>.<br>All Rights Reserved</div>

</body>
</html>
```